Wedding Program

Miriam and Owen are getting married. They are looking for a simple 4-page program that conveys the special day. Venue is a museum in a large East-Coast city: classic 18th century, formal. Ceremony is non-religious. Party includes a photo booth and DJ.

He's a math geek - she's an activist/educator.

Please incorporate unique design sensibility - be creative! Colors of purple, eggplant, ivory, and gray are the couple's choice. Fall motif OK.

Target Market(s)

ages 25 - 85, members of a family

Industry/Entity Type

Graphic Design

Font styles to use
Serif
Decorative

Colors
8769ae
b7a5cd
fece3e
f78f20
757575
cfcfcf
6b449b
a64599
fffaee

Requirements
Must have
• Readable, attractive 4-color design using the copy and image provided in the attachment.
Nice to have
• It's a LOVE-ly day for a wedding - be creative!
Should not have
• Avoid flowery girly-girl fonts or obvious hearts and flowers stuff.

```html
<!DOCTYPE html>
<html lang="en">
<head>
<meta charset="utf-8">
<title>Wedding Program – Miriam &amp; Owen</title>
<link rel="stylesheet" href="https://fonts.googleapis.com/css2?family=Norican&family=Handlee&display=swap">
<style>
  :root {
    --backdrop: #2f2f2f;
    --paper: #ffffff;
    --border-band: #d9d9d9;
    --gray-text: #757575;
    --body-text: #555555;
    --purple: #8769ae;
    --lilac: #b7a5cd;
    --gold: #fece3e;
    --orange: #f78f20;
    --script: "Norican", cursive;
    --hand: "Handlee", cursive;
  }
  * { box-sizing: border-box; margin: 0; padding: 0; }
  html, body { width: 1000px; height: 1200px; overflow: hidden; }
  body { background: var(--backdrop); position: relative; font-family: var(--hand); color: var(--body-text); }

  .page {
    position: absolute; width: 372px; height: 526px;
    background: var(--border-band);
  }
  .page--cover { left: 101px; top: 53px; }
  .page--party-a { left: 532px; top: 53px; }
  .page--party-b { left: 101px; top: 638px; }
  .page--guests { left: 532px; top: 638px; }

  .page__panel {
    position: absolute; left: 38px; right: 38px; top: 92px; bottom: 34px;
    background: var(--paper); text-align: center;
  }

  .ornament { display: block; margin: 0 auto; background: var(--lilac); border-radius: 40% 40% 50% 50%; }
  .ornament--crest { width: 72px; height: 34px; }
  .ornament--small { display: inline-block; width: 34px; height: 14px; background: #9a9a9a; vertical-align: middle; border-radius: 6px; }

  /* cover */
  .cover__top { margin-top: -40px; }
  .cover__kicker { font-family: var(--script); color: var(--gray-text); font-size: 18px; margin-top: 10px; line-height: 1; }
  .cover__of { font-size: 8px; color: var(--gray-text); }
  .cover__names { font-family: var(--script); color: var(--gold); font-size: 21px; margin-top: 14px; }
  .cover__and { font-family: var(--hand); font-size: 9px; color: var(--gray-text); }
  .cover__date { font-size: 10px; margin-top: 26px; }
  .cover__time { font-size: 10px; margin-top: 14px; }
  .cover__bottom { margin-top: 6px; }

  /* party */
  .party__title { font-family: var(--script); color: var(--orange); font-size: 20px; margin-top: 42px; }
  .party__title span.text { margin: 0 8px; vertical-align: middle; }
  .party__role { font-family: var(--script); color: var(--purple); font-size: 13px; margin-top: 11px; line-height: 1.2; }
  .party__names { font-size: 9px; line-height: 1.45; }
  .party__title + .party__role { margin-top: 6px; }

  /* guests */
  .guests__title { font-family: var(--script); color: var(--gold); font-size: 20px; margin-top: 20px; }
  .guests__copy { font-size: 9px; line-height: 1.5; padding: 0 18px; margin-top: 10px; }
  .guests__copy em { font-style: normal; color: var(--purple); font-family: var(--script); font-size: 11px; }
  .guests__photo {
    position: absolute; left: 24px; top: 238px; width: 244px; height: 108px;
    background: linear-gradient(120deg, #4e5a3a 0%, #7a6a4e 45%, #3d3a36 100%);
  }
  .guests__crest { position: absolute; left: 50%; top: 352px; transform: translateX(-50%); }
</style>
</head>
<body>

<section class="page page--cover" role="img" aria-label="Program cover with grey chevron pattern border">
  <div class="page__panel">
    <div class="cover__top"><span class="ornament ornament--crest" role="img" aria-label="Lilac scroll ornament"></span></div>
    <p class="cover__kicker">The Marriage Celebration</p>
    <p class="cover__of">of</p>
    <p class="cover__names">Miriam Calloway <span class="cover__and">and</span> Owen Marchetti</p>
    <p class="cover__date">Saturday, November 1, 2015</p>
    <p class="cover__time">At 6 pm in the evening</p>
    <div class="cover__bottom"><span class="ornament ornament--crest" role="img" aria-label="Lilac scroll ornament"></span></div>
  </div>
</section>

<section class="page page--party-a" role="img" aria-label="Wedding party page with grey chevron pattern border">
  <div class="page__panel">
    <h2 class="party__title"><span class="ornament--small" role="img" aria-label="Small scroll ornament"></span><span class="text">The Wedding Party</span><span class="ornament--small" role="img" aria-label="Small scroll ornament"></span></h2>
    <p class="party__role">Bride and Groom:</p>
    <p class="party__names">Miriam (Mimi) Calloway and Owen Marchetti</p>
    <p class="party__role">Bride's Parents:</p>
    <p class="party__names">Walter &amp; Joan Calloway</p>
    <p class="party__role">Groom's Parents:</p>
    <p class="party__names">Peter &amp; Linda Marchetti</p>
    <p class="party__role">Bridesmaids:</p>
    <p class="party__names">Nora Marchetti, Tessa Holt, Julia Brandt<br>Groomsmen Luca Marchetti, Simon Calloway, Daniel Reyes,<br>Arjun Mehta</p>
    <p class="party__role">Grandparent of the Bride:</p>
    <p class="party__names">Evelyn Hartwig</p>
    <p class="party__role">Grandparents of the Groom:</p>
    <p class="party__names">Frank Marchetti &amp; George Whitaker</p>
    <p class="party__role">Celebrant:</p>
    <p class="party__names">Clara Benning</p>
  </div>
</section>

<section class="page page--party-b" role="img" aria-label="Wedding party page with grey chevron pattern border">
  <div class="page__panel">
    <h2 class="party__title"><span class="ornament--small" role="img" aria-label="Small scroll ornament"></span><span class="text">The Wedding Party</span><span class="ornament--small" role="img" aria-label="Small scroll ornament"></span></h2>
    <p class="party__role">Bride and Groom:</p>
    <p class="party__names">Miriam (Mimi) Calloway and Owen Marchetti</p>
    <p class="party__role">Bride's Parents:</p>
    <p class="party__names">Walter &amp; Joan Calloway</p>
    <p class="party__role">Groom's Parents:</p>
    <p class="party__names">Peter &amp; Linda Marchetti</p>
    <p class="party__role">Bridesmaids:</p>
    <p class="party__names">Nora Marchetti, Tessa Holt, Julia Brandt<br>Groomsmen Luca Marchetti, Simon Calloway, Daniel Reyes,<br>Arjun Mehta</p>
    <p class="party__role">Grandparent of the Bride:</p>
    <p class="party__names">Evelyn Hartwig</p>
    <p class="party__role">Grandparents of the Groom:</p>
    <p class="party__names">Frank Marchetti &amp; George Whitaker</p>
    <p class="party__role">Celebrant:</p>
    <p class="party__names">Clara Benning</p>
  </div>
</section>

<section class="page page--guests" role="img" aria-label="Guest letter page with grey chevron pattern border">
  <div class="page__panel">
    <h2 class="guests__title">To our Wedding Guests</h2>
    <p class="guests__copy">Your presence here adds greatly to our <em>joy</em> and <em>happiness</em> on this special day</p>
    <p class="guests__copy">Today marks the beginning of our lives together. We stand before you now, declaring our love for each other and for our intent to be joined in marriage. We share with each other without reservation our lives, fortunes and future.</p>
    <p class="guests__copy">We hope that you will continue to wish us well in our new life and we are grateful to have your love, care and best wishes for today and always!</p>
    <div class="guests__photo" role="img" aria-label="Photo of the couple outdoors among tall grasses"></div>
    <span class="ornament ornament--crest guests__crest" role="img" aria-label="Lilac scroll ornament"></span>
  </div>
</section>

</body>
</html>
```